professional coaching community needs new look for website

We require a website design that attracts professionals. We run a large, global professional coaching community (e.g. executive, business, personal coaches NOT sports coaches). Our members are committed to their professional and personal development and they enjoy building relationships with other coaches across the world. We also champion the success of coaches and the coaching industry by providing business support resources to our members. We do not mind which colours you use, but whatever the combination, the combinations must be professional and refined. It would be good to have some of the familiarity of the old site colours, with some new, more professional element. We have a number of requirements for the homepage and members design, and this is attached.

Reason: I am extending the deadline for this design, in order to give feedback and see how current designs can be tweaked.

Target Market(s)

Here are some ideas for images, which gives and idea of the target market also:

Ideas for website images:

1. http://www.pixelvarno.com/stock-photo-48213077-business-success.php?st=4b2a918 (I like the people in this one – they seem very dynamic and a good mix of women and men)
2. http://www.pixelvarno.com/stock-photo-51729406-business-communications.php?st=4b2a918 (I like all of the speech bubbles in this one, that’s what the MentraLoop community does – pairs up in two’s or small groups and engages in professional talking)
3. http://www.pixelvarno.com/stock-photo-37086152-global-business-working.php?st=4b2a918 (I like the combination of the world and the people talking in different groups)
4. http://www.pixelvarno.com/stock-photo-44861039-global-business-people.php?st=e512604 (I like the world in this one – would be good to see combination of world and #1 dynamic people, which is the MentraLoop community)

Industry/Entity Type

Building

Requirements
Must have
• See attached uploaded files including homepage design, member dashboard design, and example profile (profiles need to be included him banner design). Note that any text must not be build into graphic. It needs to be able to be edited via html.

```html
<!DOCTYPE html>
<html lang="en">
<head>
<meta charset="utf-8">
<title>MentraLoop – Reciprocal peer coaching, mentoring and supervision</title>
<link href="https://fonts.googleapis.com/css2?family=PT+Sans:wght@400;700&display=swap" rel="stylesheet">
<style>
:root{
  --teal:#2f7b90;
  --teal-dark:#22667a;
  --green:#86c98a;
  --green-strip:#8fcb8c;
  --sage:#b5ccc3;
  --sage-light:#e2ede9;
  --ink:#333;
  --muted:#7a7a7a;
  --orange:#f0641e;
  --white:#fff;
  --page-bg:#f1f1f1;
}
*{box-sizing:border-box;margin:0;padding:0}
html,body{width:819px;height:1200px;overflow:hidden}
body{position:relative;font-family:"PT Sans",Arial,sans-serif;color:var(--ink);font-size:11px;
  background:linear-gradient(var(--teal) 0 230px,var(--page-bg) 230px 965px,var(--teal) 965px 1170px,var(--green-strip) 1170px)}
.abs{position:absolute}
.page{position:absolute;left:96px;top:10px;width:627px;height:968px;background:var(--white);border-radius:5px}
/* header */
.brand{left:115px;top:44px;font-size:15px;font-weight:700;color:var(--teal)}
.brand-mark{display:inline-block;width:10px;height:10px;border-radius:50%;background:var(--teal);margin-right:5px}
.tagline{left:140px;top:60px;font-size:7.5px;color:var(--teal-dark);line-height:9px;font-style:italic}
.call{left:508px;top:27px;font-size:9px;color:var(--teal)}
.phone{left:508px;top:36px;font-size:14px;color:var(--teal)}
.flags{left:625px;top:38px;display:flex;gap:2px}
.flag{width:15px;height:10px;display:flex}
.flag i{flex:1}
.nav-item{position:absolute;top:68px;height:26px;line-height:27px;font-size:12px;color:#888;text-decoration:none;text-transform:uppercase;white-space:nowrap}
.nav-item.active{left:305px;width:64px;text-align:center;background:var(--teal);color:var(--white)}
.nav-rule{left:102px;top:94px;width:615px;height:2px;background:var(--teal)}
/* hero */
.hero{left:102px;top:96px;width:414px;height:134px;
  background:
    radial-gradient(ellipse 120px 28px at 150px 18px,rgba(38,150,165,.75),transparent 70%),
    radial-gradient(ellipse 90px 22px at 330px 14px,rgba(38,150,165,.7),transparent 70%),
    linear-gradient(180deg,transparent 0 45px,rgba(20,30,35,.8) 45px 110px,transparent 110px) 60px 0/300px 134px no-repeat,
    linear-gradient(180deg,#7cc0cb 0%,#d3e9ec 50%,#eef4f5 100%)}
.hero-caption{left:102px;top:207px;width:414px;height:23px;background:rgba(47,123,144,.85);color:var(--white);font-size:13.5px;font-weight:700;line-height:23px;padding-left:10px;white-space:nowrap}
/* login */
.login{left:517px;top:96px;width:200px;height:134px;background:var(--green)}
.panel-title{color:var(--white);font-size:14px;font-weight:700;text-transform:uppercase}
.field{position:absolute;background:var(--white);border-radius:3px;font-size:9.5px;color:#777;padding-left:7px;line-height:24px;height:24px}
.btn-login{left:530px;top:199px;width:42px;height:19px;background:var(--orange);color:var(--white);font-size:9px;font-weight:700;line-height:19px;text-align:center}
/* why box */
.why-bg{left:102px;top:230px;width:414px;height:148px;background:var(--sage-light)}
.why{left:115px;top:243px;width:389px;height:123px;background:var(--white)}
.why h2{height:33px;line-height:33px;padding-left:13px;font-size:13.5px;color:var(--teal-dark);background:linear-gradient(#fff,#eee);text-transform:uppercase;white-space:nowrap}
.why-list{position:absolute;left:12px;top:41px;display:grid;grid-template-columns:135px 135px 120px;row-gap:5px;list-style:none}
.why-list li{font-size:10.5px;color:#444;line-height:14px;padding-left:9px;position:relative;white-space:nowrap}
.why-list li::before{content:"";position:absolute;left:0;top:4px;border-left:4px solid var(--teal);border-top:3px solid transparent;border-bottom:3px solid transparent}
/* signup */
.signup{left:517px;top:230px;width:200px;height:356px;background:var(--teal)}
.signup-inner{left:527px;top:265px;width:180px;height:313px;background:var(--sage)}
.perks{position:absolute;left:535px;top:272px;list-style:none;width:160px}
.perks li{font-size:9px;color:#234;line-height:11px;padding-left:9px;position:relative;margin-bottom:10px}
.perks li::before{content:"";position:absolute;left:0;top:3px;border-left:3px solid #234;border-top:2.5px solid transparent;border-bottom:2.5px solid transparent}
.terms{left:536px;top:505px;font-size:9px;color:#234;line-height:13px}
.terms .box{display:inline-block;width:9px;height:9px;background:var(--white);border:1px solid #999;margin-right:7px;vertical-align:-1px}
.btn-signup{left:536px;top:536px;width:162px;height:31px;border-radius:4px;background:linear-gradient(#f58a3e,#e4560f);color:var(--white);font-size:15px;font-weight:700;text-align:center;line-height:31px}
.promo{left:517px;top:593px;width:200px;height:93px;background:linear-gradient(180deg,#5f8db0 0%,#d9a46b 60%,#b8672f 100%)}
.promo-text{left:517px;top:650px;width:200px;text-align:center;font-size:14px;font-weight:700;color:#f6a623}
/* supporters */
.sup-head{left:517px;top:692px;width:200px;height:31px;background:var(--teal);line-height:31px;padding-left:14px}
.sup-box{left:517px;top:723px;width:200px;height:219px;border:1px solid #e4e4e4}
.sup-grid{position:absolute;left:521px;top:733px;display:grid;grid-template-columns:96px 96px;grid-auto-rows:58px}
.sup-grid div{display:flex;align-items:center;justify-content:center;border-right:1px dotted #ddd;border-bottom:1px dotted #ddd}
.sup-grid div:nth-child(2n){border-right:0}
.sup-grid div:nth-child(n+5){border-bottom:0}
.badge{background:#9a9a9a}
.sup-more{left:527px;top:918px;font-size:9.5px;color:#444}
.sup-more a{color:var(--teal);text-decoration:underline}
/* video */
.section-title{font-size:14px;font-weight:700;color:var(--teal-dark);text-transform:uppercase;white-space:nowrap}
.arrows{left:472px;top:402px;display:flex;gap:2px}
.arrows span{width:13px;height:13px;border:1px solid #ccc;background:#f4f4f4;display:flex;align-items:center;justify-content:center}
.video-frame{left:102px;top:425px;width:401px;height:239px;background:#ececec;border:1px solid #ddd}
.video{left:121px;top:443px;width:365px;height:204px;background:linear-gradient(135deg,#6d7073 0%,#3c3f42 50%,#1e1f21 100%)}
.video-tools{left:451px;top:449px;width:28px;display:flex;flex-direction:column;gap:2px}
.video-tools span{height:25px;background:rgba(0,0,0,.65);color:var(--white);font-size:4.5px;text-align:center;padding-top:3px}
.video-bar{left:127px;top:617px;width:353px;height:24px;background:rgba(0,0,0,.7)}
/* welcome */
.welcome-title{left:109px;top:686px}
.welcome-rule{left:109px;top:707px;width:384px;height:1px;background:#e3e3e3}
.welcome-copy{left:109px;top:716px;width:388px;font-size:10px;line-height:15.4px;color:#444}
.welcome-copy p+p{margin-top:15px}
/* footer */
.footer{left:96px;top:985px;width:627px;height:178px;background:var(--sage);border-radius:3px}
.fcol{position:absolute;top:995px}
.fcol h3{font-size:12.5px;font-weight:400;color:#234;margin-bottom:8px;text-transform:uppercase}
.fcol a{display:block;font-size:9.5px;color:#234;text-decoration:none;line-height:19.2px}
.contact p{font-size:9.5px;color:#234;line-height:13px;margin-bottom:9px}
.social{left:594px;top:1109px;display:flex;gap:6px}
.social span{width:18px;height:18px;border-radius:50%;background:var(--teal)}
.legal{left:109px;top:1179px;font-size:9px;color:#234}
.legal-links{left:555px;top:1179px;font-size:9px;color:#234}
</style>
</head>
<body>
<div class="page"></div>

<header>
  <div class="abs brand"><span class="brand-mark"></span>MentraLoop</div>
  <div class="abs tagline">Reciprocal peer coaching,<br>mentoring and supervision</div>
  <div class="abs call">Call Now</div>
  <div class="abs phone">(123) 5550-4821</div>
  <div class="abs flags">
    <span class="flag"><i style="background:#2a3f8f"></i><i style="background:#c8102e"></i><i style="background:#2a3f8f"></i></span>
    <span class="flag"><i style="background:#009246"></i><i style="background:#fff"></i><i style="background:#ce2b37"></i></span>
    <span class="flag" style="flex-direction:column"><i style="background:#000"></i><i style="background:#d00"></i><i style="background:#fc0"></i></span>
    <span class="flag"><i style="background:#0055a4"></i><i style="background:#fff"></i><i style="background:#ef4135"></i></span>
    <span class="flag" style="flex-direction:column"><i style="background:#c60b1e"></i><i style="background:#fff"></i><i style="background:#c60b1e"></i></span>
  </div>
  <nav>
    <a class="nav-item active" href="#">Join Us</a>
    <a class="nav-item" href="#" style="left:387px">Coaching</a>
    <a class="nav-item" href="#" style="left:464px">Mentoring</a>
    <a class="nav-item" href="#" style="left:551px">Supervision</a>
    <a class="nav-item" href="#" style="left:643px">Resources</a>
  </nav>
  <div class="abs nav-rule"></div>
</header>

<div class="abs hero" role="img" aria-label="Silhouettes of business people talking in groups in front of a world map"></div>
<div class="abs hero-caption">JOIN THE MOST DYNAMIC COACHIN COMMUNITY IN THE WORD</div>

<section class="abs login">
  <svg class="abs" style="left:13px;top:11px" width="14" height="16" viewBox="0 0 14 16"><circle cx="7" cy="4.5" r="4" fill="#fff"/><path d="M0 16c0-5 3-7 7-7s7 2 7 7z" fill="#fff"/></svg>
  <div class="abs panel-title" style="left:34px;top:11px;font-size:15px">Member Login</div>
</section>
<div class="field" style="left:530px;top:134px;width:175px">User Name</div>
<div class="field" style="left:530px;top:165px;width:175px">Password</div>
<div class="abs btn-login">LOGIN</div>

<div class="abs why-bg"></div>
<section class="abs why">
  <h2>Why are there xxxx MentraLoop coaches?</h2>
  <ul class="why-list">
    <li>Lorem ipsum dolor</li><li>Lorem ipsum dolor</li><li>Lorem ipsum dolor</li>
    <li>Nulla blandit quam</li><li>Nulla blandit quam</li><li>Nulla blandit quam</li>
    <li>Nulla convallis elit</li><li>Nulla convallis elit</li><li>Nulla convallis elit</li>
    <li>Aliquam sodales</li><li>Aliquam sodales</li><li>Aliquam sodales</li>
  </ul>
</section>

<section class="abs signup"><div class="abs panel-title" style="left:10px;top:10px">Quick Signup</div></section>
<div class="abs signup-inner"></div>
<ul class="perks">
  <li>Free to Join</li>
  <li>3 Issues of Coaching Research<br>in Practice</li>
  <li>Monthly issues of Lessons from<br>the field</li>
  <li>Access to our Community</li>
  <li>Online Profile</li>
</ul>
<div class="field" style="left:535px;top:407px;width:163px">First Name</div>
<div class="field" style="left:535px;top:437px;width:163px">Last Name</div>
<div class="field" style="left:535px;top:467px;width:163px">Email Address</div>
<div class="abs terms"><span class="box"></span>I have read the MentraLoop<br><span style="padding-left:16px">terms and conditions</span></div>
<div class="abs btn-signup">SIGNUP NOW</div>

<div class="abs promo" role="img" aria-label="Silhouettes of people raising their arms against a sunset sky"></div>
<div class="abs promo-text">REGISTRATION IS OPEN !</div>

<div class="abs sup-head panel-title">Our Supporters</div>
<div class="abs sup-box"></div>
<div class="sup-grid">
  <div><span class="badge" style="width:46px;height:46px;border-radius:50%"></span></div>
  <div><span class="badge" style="width:40px;height:40px;border-radius:50%"></span></div>
  <div><span class="badge" style="width:70px;height:18px"></span></div>
  <div><span class="badge" style="width:56px;height:24px;border-radius:12px"></span></div>
  <div><span class="badge" style="width:48px;height:30px;border-radius:50%"></span></div>
  <div><span class="badge" style="width:40px;height:40px;border-radius:50%"></span></div>
</div>
<div class="abs sup-more"><a href="#">Click Here </a>to see more of our supporters</div>

<div class="abs section-title" style="left:108px;top:398px">Our Video</div>
<div class="abs arrows">
  <span><svg width="5" height="7"><path d="M4 0L0 3.5 4 7" fill="none" stroke="#777"/></svg></span>
  <span><svg width="5" height="7"><path d="M1 0l4 3.5L1 7" fill="none" stroke="#777"/></svg></span>
</div>
<div class="abs video-frame"></div>
<div class="abs video" role="img" aria-label="Video still of business people meeting around a laptop"></div>
<div class="abs video-tools"><span>LIKE</span><span>LATER</span><span>SHARE</span><span>EMBED</span></div>
<div class="abs video-bar">
  <svg class="abs" style="left:16px;top:6px" width="10" height="12"><path d="M0 0l10 6-10 6z" fill="#fff"/></svg>
  <div class="abs" style="left:55px;top:9px;width:222px;height:6px;background:#555"><div style="width:64px;height:6px;background:#2a9fd6"></div></div>
  <div class="abs" style="left:310px;top:7px;font-size:9px;font-weight:700;color:#2a9fd6;font-style:italic">HD</div>
</div>

<div class="abs section-title welcome-title">Welcome to MentraLoop</div>
<div class="abs welcome-rule"></div>
<div class="abs welcome-copy">
  <p>Lorem ipsum dolor sit amet, consectetur adipisicing elit, sed do all of eiusmod tempor incididunt ut labore et dolore magna aliqua. Ut enim ad minim veniam, quis nostrud exercitation ullamco laboris nisi ut aliquip ex ea and commodo consequat. Duis aute irure dolor in reprehenderit in voluptate velit esse cillum dolore eu fugiat nulla pariatur. Sed ut perspiciatis unde omnis iste natus error sit voluptatem accusantium doloremque laudantium, totam rem asd aperiam. Excepteur sint occaecat cupidatat non proident, sunt in all of culpa qui officia deserunt mollit anim id est sint occaecat cupidatat non proident, sunt in culpa qui officia deserunt mollit anim id est laborum.</p>
  <p>Lorem ipsum dolor sit amet, consectetur adipisicing elit, sed do eiusmod tempor incididunt ut labore et dolore magna aliqua. Ut enim ad minim veniam, quis nostrud exercitation ullamco laboris nisi ut aliquip ex ea all dafcommodo consequat. Duis aute irure dolor in reprehenderit in voluptate velit esse cillum dolore eu fugiat nulla pariatur. Lorem ipsum dolor sit amet, consectetur adipisicing elit, sed do eiusmod tempor incididunt ut labore et dolore magna aliqua Sunt.</p>
</div>

<footer>
  <div class="abs footer"></div>
  <div class="fcol" style="left:109px"><h3>Join Us</h3><a href="#">Sign up</a><a href="#">Annual membership</a><a href="#">Pay-as-You-go</a><a href="#">FAQs</a><a href="#">Our team</a><a href="#">Our history</a><a href="#">Make Contact</a></div>
  <div class="fcol" style="left:222px"><h3>Coaching</h3><a href="#">What it is</a><a href="#">Benefits For You</a><a href="#">In-built features</a><a href="#">Testimonials</a><a href="#">FAQS</a><a href="#">Upcomming rounds</a></div>
  <div class="fcol" style="left:339px"><h3>Mentoring</h3><a href="#">What it is</a><a href="#">Benefits For You</a><a href="#">In-built features</a><a href="#">Testimonials</a><a href="#">FAQS</a><a href="#">Upcomming rounds</a></div>
  <div class="fcol" style="left:463px"><h3>Supervision</h3><a href="#">What it is</a><a href="#">Benefits For You</a><h3 style="margin-top:12px">Resources</h3><a href="#">Benefits For You</a><a href="#">In-built features</a></div>
  <div class="fcol contact" style="left:571px;width:145px"><h3>Contact Us</h3>
    <p>Address : 151 Lorem ipsum dolor<br><span style="padding-left:41px">sit amet, consectetur.</span></p>
    <p>Email ID : hello@mentraloop.net</p>
    <p>Phone : <span style="font-size:13px">(123) 5550-4821</span></p>
  </div>
  <div class="abs social"><span></span><span></span><span></span><span></span><span></span></div>
  <div class="abs legal">Copyright © 2013 MentraLoop Pty Ltd. All Rights Reserved.</div>
  <div class="abs legal-links">MentraLoop Privacy Policy &nbsp;/&nbsp; Sitemap</div>
</footer>
</body>
</html>
```